Fore Sale sign for my real estate agency

I am a Brisbane - Australia inner western suburbs boutique real estate agent who is needing a for sale sign. We are a small dynamic family agency that needs a for sale sign that will standout and give us a strong presence in the market.

I have attached a logo I like, however I am not fixed on anything and am open to suggestions.

The information on the sign should contain but not necessarily limited to the following information - please appreciate I am very open
1 logo - Vellman
2 Ph number - 3847 1593
3 web address - vellman.example.au

Thank you
Glen Vellman

```html
<!DOCTYPE html>
<html lang="en">
<head>
<meta charset="utf-8">
<title>Vellman – For Sale Sign</title>
<link href="https://fonts.googleapis.com/css2?family=Arimo:wght@700&family=Tinos:wght@400&display=swap" rel="stylesheet">
<style>
  :root {
    --ink: #000000;
    --paper: #ffffff;
    --brand-dark: #262626;
    --accent-red: #e0161b;
    --accent-orange: #d94a0b;
  }
  * { margin: 0; padding: 0; box-sizing: border-box; }
  html, body {
    width: 1200px;
    height: 900px;
    overflow: hidden;
    background: var(--paper);
  }
  .sign {
    position: relative;
    width: 1200px;
    height: 900px;
    background: var(--paper);
  }
  .headline-band {
    position: absolute;
    top: 0; left: 0;
    width: 1200px;
    height: 293px;
    background: var(--ink);
    display: flex;
    align-items: center;
    justify-content: center;
  }
  .headline {
    font-family: "Arimo", Arial, sans-serif;
    font-weight: 700;
    font-size: 214px;
    letter-spacing: 0;
    color: var(--paper);
    line-height: 1;
    transform: translateY(6px);
  }
  .brand {
    position: absolute;
    top: 432px;
    left: 0;
    width: 1200px;
    text-align: center;
  }
  .brand-name {
    font-family: "Arimo", Arial, sans-serif;
    font-weight: 700;
    font-size: 92px;
    line-height: 1;
    color: var(--brand-dark);
  }
  .contact-line {
    position: absolute;
    top: 560px;
    left: 0;
    width: 1200px;
    display: flex;
    align-items: center;
    justify-content: center;
    font-family: "Tinos", "Times New Roman", serif;
    font-size: 43px;
    line-height: 1;
  }
  .call-now { color: var(--ink); }
  .divider {
    display: inline-block;
    width: 2px;
    height: 50px;
    background: var(--ink);
    margin: 0 26px 0 36px;
  }
  .agent-name { color: var(--accent-red); }
  .phone {
    position: absolute;
    top: 612px;
    left: 0;
    width: 1200px;
    text-align: center;
    font-family: "Tinos", "Times New Roman", serif;
    font-size: 156px;
    line-height: 1;
    color: var(--ink);
  }
  .web-band {
    position: absolute;
    left: 0;
    bottom: 0;
    width: 1200px;
    height: 113px;
    background: var(--accent-orange);
    display: flex;
    align-items: center;
    justify-content: center;
  }
  .web-address {
    font-family: "Tinos", "Times New Roman", serif;
    font-size: 58px;
    color: var(--paper);
    line-height: 1;
  }
</style>
</head>
<body>
  <main class="sign">
    <header class="headline-band">
      <h1 class="headline">FOR SALE</h1>
    </header>

    <div class="brand">
      <span class="brand-name">Vellman</span>
    </div>

    <p class="contact-line">
      <span class="call-now">CALL NOW</span>
      <span class="divider" aria-hidden="true"></span>
      <span class="agent-name">Glen Vellman</span>
    </p>

    <p class="phone">3847 1593</p>

    <footer class="web-band">
      <span class="web-address">www.vellman.example.au</span>
    </footer>
  </main>
</body>
</html>
```